Business Card design project for new family-run construction business

We need a logo and business card designed for a new construction company. We want to convey a professional, but approachable image. We hope to be servicing small residential clients as well as large commercial contracts as well.
Our business will employ a single "Hydro excavator" truck, which can be used for multiple purposes: vacuuming up dirt or water, digging holes, clearing sewer blockages and so on.
We are open to different colour schemes, however blue and white, or yellow/green would be good combinations. We are open to multiple colours (2-4), so long as they are complimentary.

EDIT: Let's not put much emphasis on the octopus... unless it's very clear that the arms are actual vacuum hoses, it won't make sense. An octopus on it's own has little to do with our business.

Please also do not use actual photos of hydro-vac trucks. This is not the aesthetic we are going for.

**The logo should instead be: A stylized outline of a hydrovac truck (a line drawing or digital version of a line-drawing). See the two examples in the attached images of hydrovac trucks. I've also included a very crude pen outline as a reference. Please use your artistic discretion and talent (as I clearly have none) to make something that looks much nicer. Thanks for your efforts!**

The front of the card should have the following elements:
Logo
Name: P & K Hydro Excavation and Flushign
Two phone numbers: Direct and Office
Email address
Website
It should also have the name of the employee and their job title
At the bottom of the card it should say (in a noticeable way): "24/7 Emergency Calls Welcome"

The back of the card should have the following elements:
"20 Years Experience"
"A Canadian Family Run Business"
A small maple-leaf logo that is in a similar style to the rest of the card/logos in the bottom right corner of the back of the card. (see attached)

**We have just added a number of business card designs that really appeal to us to offer inspiration.**

Reason: We have not received designs that hit the mark of what we are looking for. Feedback has been posted, so we would like to provide the designers more time.

Target Market(s)

Commercial and residential customers. As big as large malls and office buildings, as small single-family home owners

Industry/Entity Type

Construction Company

Contact Information for Business Card

We have just added a number of business card designs that really appeal to us to offer inspiration.

Logo
Email address
Website

"20 Years Experience"

Logo Text

P & K Hydro Excavation and Flushing

Font styles to use
Serif
Sans Serif
Other font styles liked:
• Helvetica, Futura, Impact, bold strong, modern fonts that convey a sense of design and style

Colors
0592cd
ec1f27
9bcb3c

Requirements
Must have
• The front of the card should have the following elements:
• Logo
• Name: P & K Hydro Excavation and Flushign
• Two phone numbers: Direct and Office
• Email address
• Website
• It should also have the name of the employee and their job title
• At the bottom of the card it should say (in a noticeable way): "24/7 Emergency Calls Welcome"
• The back of the card should have the following elements:
• "20 Years Experience"
• "A Canadian Family Run Business"
• A small maple-leaf logo that is in a similar style to the rest of the card/logos in the bottom right corner of the back of the card. (see attached)
Nice to have
• The card does not have to be a perfect rectangle. We are open to rounded corners or cut out elements.
• Also embossing, engraving, adding highlighted/glossy layers (spot glass?), or any other effect that will give the card a unique look/feel is more than welcome.
• We would love to have a card that stands out from others and is compelling to look at it, so we are happy to incorporate any sort of modern printing technology to bring out the design.
• Please feel encouraged to be creative and design something unique, especially for this industry.
• Our dream would be if a Scandinavian architect were to go into the construction business and design this business card ;)
Should not have
• Photographs

```html
<!DOCTYPE html>
<html lang="en">
<head>
<meta charset="utf-8">
<title>P &amp; K Hydro Excavation and Flushing – Business Card</title>
<link href="https://fonts.googleapis.com/css2?family=Michroma&family=Oswald:wght@500&family=Roboto:wght@400&display=swap" rel="stylesheet">
<style>
  :root {
    --brand-red: #d41f27;
    --card-white: #ffffff;
    --stage: #8c8c8c;
    --stage-light: #b4b4b4;
    --text-red: #d41f27;
  }
  * { margin: 0; padding: 0; box-sizing: border-box; }
  html, body { width: 1200px; height: 900px; overflow: hidden; }
  body {
    background: linear-gradient(180deg, var(--stage-light) 0%, var(--stage) 100%);
    position: relative;
    font-family: "Roboto", Arial, sans-serif;
  }
  .card {
    position: absolute;
    top: 300px;
    width: 520px;
    height: 300px;
    border-radius: 22px;
    overflow: hidden;
    box-shadow: 0 10px 24px rgba(0,0,0,.25);
  }

  /* Back */
  .card-back { left: 50px; background: var(--brand-red); color: var(--card-white); }
  .back-tagline {
    position: absolute; left: 0; right: 0; top: 118px;
    text-align: center; font-family: "Michroma", "Arial", sans-serif;
  }
  .back-tagline .headline { font-size: 19px; letter-spacing: 2px; }
  .back-tagline .subline { font-size: 13px; letter-spacing: 2.5px; margin-top: 16px; }
  .heritage-badge {
    position: absolute; right: 36px; bottom: 34px;
    width: 40px; height: 40px; border-radius: 50%;
    border: 3px solid var(--card-white);
  }

  /* Front */
  .card-front { left: 630px; background: var(--card-white); }
  .company-name {
    position: absolute; left: 30px; top: 90px; width: 240px;
    font-family: "Oswald", "Arial Narrow", sans-serif; font-weight: 500;
    color: var(--text-red); font-size: 27px; line-height: 1.2;
    text-align: center; text-transform: uppercase;
  }
  .divider {
    position: absolute; left: 290px; top: 70px; width: 2px; height: 150px;
    background: var(--brand-red);
  }
  .staff { position: absolute; left: 310px; top: 76px; color: var(--text-red); }
  .staff .name { font-size: 18px; }
  .staff .role { font-size: 12px; margin-top: 4px; }
  .contacts {
    position: absolute; left: 310px; top: 140px; list-style: none;
    color: var(--text-red); font-size: 13px; line-height: 18px;
  }
  .contacts li { display: flex; align-items: center; gap: 5px; }
  .contacts svg { width: 12px; height: 12px; flex: none; }
  .emergency-band {
    position: absolute; left: 0; right: 0; bottom: 28px; height: 18px;
    background: var(--brand-red); color: var(--card-white);
    font-size: 10px; letter-spacing: 9px; text-transform: uppercase;
    display: flex; align-items: center; justify-content: center;
  }
</style>
</head>
<body>

  <section class="card card-back" aria-label="Card back">
    <div class="back-tagline">
      <p class="headline">20 YEARS EXPERIENCE</p>
      <p class="subline">A CANADIAN FAMILY RUN BUSINESS</p>
    </div>
    <div class="heritage-badge" aria-hidden="true"></div>
  </section>

  <section class="card card-front" aria-label="Card front">
    <h1 class="company-name">P &amp; K Hydro Excavation and Flushing</h1>
    <div class="divider"></div>
    <div class="staff">
      <p class="name">Dana Holt</p>
      <p class="role">Manager</p>
    </div>
    <ul class="contacts">
      <li>
        <svg viewBox="0 0 12 12" aria-hidden="true"><rect x="3" y="0.5" width="6" height="11" rx="1" fill="none" stroke="currentColor"/><circle cx="6" cy="9.5" r=".8" fill="currentColor"/></svg>
        555-014-2901
      </li>
      <li>
        <svg viewBox="0 0 12 12" aria-hidden="true"><path d="M2.5 1 L4.5 1 L5.2 3.6 L4 4.6 Q5 7 7.4 8 L8.4 6.8 L11 7.5 L11 9.5 Q10.5 11 9 11 Q1 10 1 3 Q1 1.5 2.5 1Z" fill="currentColor"/></svg>
        555-014-2922
      </li>
      <li>
        <svg viewBox="0 0 12 12" aria-hidden="true"><rect x="0.5" y="2" width="11" height="8" fill="currentColor"/><path d="M0.5 2 L6 6.5 L11.5 2" fill="none" stroke="#fff"/></svg>
        dana@pkhydroexflush.com
      </li>
      <li>
        <svg viewBox="0 0 12 12" aria-hidden="true"><circle cx="6" cy="6" r="5.3" fill="none" stroke="currentColor"/><ellipse cx="6" cy="6" rx="2.3" ry="5.3" fill="none" stroke="currentColor"/><path d="M0.7 6 H11.3" stroke="currentColor"/></svg>
        pkhydroexflush.com
      </li>
    </ul>
    <div class="emergency-band">24/7 Emergency Calls Welcome</div>
  </section>

</body>
</html>
```